Robotic startup business cards

We are looking for a design for a set of business cards which reflect the spirit and humor of Torvexa Robotics. We want to present ourselves as sleek, professional, but laid-back consulting company.

We primarily focus on developing robotic arms software. This software controls robots and does things like grab items, pick objects up, move them, etc.

We want to allow you maximum design creativity, but do ask that you consider our existing style guidelines (see attached files) in order to make our brand cohesive.

Target Market(s)

Startups and Mid-size robotic companies

Industry/Entity Type

Business

Contact Information for Business Card

Liam Brantly, PhD
Roboticist | Torvexa Consulting | 318.572.6094

Font styles to use
Other font styles liked:
• Source code pro

Requirements
Must have
• robots or robotic arms
• similar color scheme that works with existing brand guidelines
Nice to have
• please consider our existing style guidelines (see attached files) in order to make our brand cohesive.
• minimalism style is generally nice.
Should not have
• An old, boring, or corporate feel. Too much text.

```html
<!DOCTYPE html>
<html lang="en">
<head>
<meta charset="utf-8">
<title>Torvexa Robotics – Business Cards</title>
<link href="https://fonts.googleapis.com/css2?family=Fira+Sans+Condensed:ital,wght@1,300;1,400&family=Source+Code+Pro:wght@400&display=swap" rel="stylesheet">
<style>
  :root {
    --backdrop: #e6e6e3;
    --card-black: #000000;
    --brand-green: #4fb381;
    --tab-green: #3e8f64;
    --paper-white: #ffffff;
    --paper-grey: #c9c9c9;
    --icon-grey: #b5b5b5;
    --text-white: #f4f4f4;
  }
  html, body {
    margin: 0;
    padding: 0;
    width: 1200px;
    height: 900px;
    overflow: hidden;
    background: var(--backdrop);
  }
  .canvas {
    position: relative;
    width: 1200px;
    height: 900px;
  }
  .card {
    position: absolute;
    box-shadow: 0 3px 6px rgba(0,0,0,0.35);
    overflow: hidden;
  }
  /* front */
  .card-front {
    left: 186px;
    top: 227px;
    width: 393px;
    height: 235px;
    background: var(--card-black);
  }
  .mascot {
    position: absolute;
    left: 68px;
    top: 55px;
    width: 84px;
    height: 112px;
    border-radius: 40px 40px 30px 30px;
    background: radial-gradient(circle at 50% 35%, #e6e6e6 0%, #9a9a9a 55%, #1a1a1a 100%);
  }
  .front-wordmark {
    position: absolute;
    left: 220px;
    top: 101px;
    margin: 0;
    font-family: "Source Code Pro", monospace;
    font-weight: 400;
    font-size: 17px;
    letter-spacing: 3px;
    color: var(--text-white);
    display: flex;
    align-items: center;
    gap: 10px;
  }
  .front-wordmark .dot {
    width: 10px;
    height: 10px;
    border-radius: 50%;
    background: var(--brand-green);
  }
  .edge-tab {
    position: absolute;
    right: 0;
    top: 75px;
    width: 19px;
    height: 75px;
    background: var(--tab-green);
  }
  /* back */
  .card-back {
    left: 538px;
    top: 477px;
    width: 388px;
    height: 227px;
    background: linear-gradient(200deg, var(--paper-white) 25%, var(--paper-grey) 100%);
  }
  .name-band {
    position: absolute;
    left: 0;
    top: 69px;
    width: 100%;
    height: 81px;
    background: var(--card-black);
  }
  .band-wordmark {
    position: absolute;
    left: 24px;
    top: 28px;
    margin: 0;
    font-family: "Source Code Pro", monospace;
    font-size: 18px;
    letter-spacing: 2px;
    color: var(--brand-green);
  }
  .person-name {
    position: absolute;
    right: 32px;
    top: 28px;
    margin: 0;
    font-family: "Fira Sans Condensed", sans-serif;
    font-style: italic;
    font-weight: 300;
    font-size: 19px;
    letter-spacing: 1.5px;
    color: var(--text-white);
  }
  .contact-line {
    position: absolute;
    left: 22px;
    top: 158px;
    margin: 0;
    font-family: "Fira Sans Condensed", sans-serif;
    font-style: italic;
    font-weight: 400;
    font-size: 12.5px;
    letter-spacing: 2.6px;
    color: var(--brand-green);
    white-space: nowrap;
  }
  .service-icons {
    position: absolute;
    left: 30px;
    top: 190px;
    display: flex;
    gap: 20px;
  }
  .service-icons svg {
    width: 20px;
    height: 20px;
    stroke: var(--icon-grey);
    fill: none;
    stroke-width: 1.4;
  }
</style>
</head>
<body>
<main class="canvas">
  <section class="card card-front">
    <div class="mascot" role="img" aria-label="Friendly cartoon robot mascot hovering on a rocket flame"></div>
    <h1 class="front-wordmark"><span class="dot"></span>TORVEXA</h1>
    <div class="edge-tab"></div>
  </section>

  <section class="card card-back">
    <div class="name-band">
      <p class="band-wordmark">TORVEXA</p>
      <h2 class="person-name">Liam Brantly, PhD</h2>
    </div>
    <p class="contact-line">Roboticist | Torvexa Consulting | 318.572.6094</p>
    <div class="service-icons">
      <svg viewBox="0 0 20 20"><circle cx="4" cy="5" r="2"/><circle cx="15" cy="4" r="2"/><circle cx="10" cy="15" r="2"/><path d="M5.5 6.5 9 13.5M13.5 5.5 11 13"/></svg>
      <svg viewBox="0 0 20 20"><path d="M10 3v8M10 11l-7 5M10 11l7 5"/></svg>
      <svg viewBox="0 0 20 20"><rect x="5" y="5" width="10" height="10"/><rect x="8" y="8" width="4" height="4"/><path d="M7 2v3M13 2v3M7 15v3M13 15v3"/></svg>
      <svg viewBox="0 0 20 20"><circle cx="7" cy="10" r="5"/><circle cx="13" cy="10" r="5"/></svg>
      <svg viewBox="0 0 20 20" style="fill:var(--icon-grey);stroke:none"><circle cx="4" cy="4" r="1.8"/><circle cx="10" cy="4" r="1.8"/><circle cx="16" cy="4" r="1.8"/><circle cx="4" cy="10" r="1.8"/><circle cx="10" cy="10" r="1.8"/><circle cx="16" cy="10" r="1.8"/><circle cx="4" cy="16" r="1.8"/><circle cx="10" cy="16" r="1.8"/><circle cx="16" cy="16" r="1.8"/></svg>
      <svg viewBox="0 0 20 20"><path d="M18 2 2 9l7 2 2 7z"/></svg>
      <svg viewBox="0 0 20 20"><rect x="2" y="4" width="16" height="12" rx="1"/><circle cx="7" cy="10" r="2.2"/><circle cx="13" cy="10" r="2.2"/></svg>
      <svg viewBox="0 0 20 20"><circle cx="10" cy="10" r="3"/><path d="M10 2v3M10 15v3M2 10h3M15 10h3M4.3 4.3l2.1 2.1M13.6 13.6l2.1 2.1M4.3 15.7l2.1-2.1M13.6 6.4l2.1-2.1"/></svg>
      <svg viewBox="0 0 20 20"><path d="M2 3h16v11H7l-4 3v-3H2z"/><path d="M5 7h10M5 10h8"/></svg>
    </div>
  </section>
</main>
</body>
</html>
```